Personal Finance e-commerce website needs a simple budget design

Hello! I am starting to sell downloadable and printable budget planners, as shown in the attached file, for people to plan ahead on their personal finances. <br/><br/>I want to see a one-page design with similar columns (for example, "Expenses, Budget, and Actual"). I would also like to see the basic formula ("Net Income = Gross income - Total Expenses") somewhere on the design. Finally, I want the design to remain mostly minimalistic and simple for the average person to plan their personal monthly budgets.<br/><br/>However, other than that, the overall design, layout, and colors will be at the graphic designer's choice. If you have any questions for me, please let me know. Thank you for your time!

Industry/Entity Type

Financial Planning

Colors

Designer to choose colors to be used in the design.

Requirements
Must have
• I want to see a one-page design with similar columns (for example, "Expenses, Budget, and Actual").
• I want the design to remain mostly minimalistic and simple for the average person to plan their personal monthly budgets.
Nice to have
• I would also like to see the basic formula ("Net Income = Gross income - Total Expenses") somewhere on the design.

```html
<!DOCTYPE html>
<html lang="en">
<head>
<meta charset="utf-8">
<title>Basic Monthly Budget Planner</title>
<link href="https://fonts.googleapis.com/css2?family=Archivo:wght@400;500;600;700;800&family=Didact+Gothic&display=swap" rel="stylesheet">
<style>
  :root {
    --green: #8fae1b;
    --green-bright: #b3cc2c;
    --leaf: #cbd89a;
    --pink: #ef5f6b;
    --grey: #a9a9a9;
    --ink-soft: #9a9a9a;
    --frame: #c4c4c4;
    --paper: #ffffff;
  }
  * { margin: 0; padding: 0; box-sizing: border-box; }
  html, body { width: 848px; height: 1200px; overflow: hidden; background: var(--paper); }
  .planner {
    position: relative; width: 848px; height: 1200px; overflow: hidden;
    background: var(--paper); font-family: "Archivo", Arial, sans-serif;
  }
  .side-label {
    position: absolute; color: var(--pink); font-size: 25px; font-weight: 400;
    transform: rotate(-90deg); transform-origin: left top; line-height: 1;
  }
  .side-label--basic { left: 34px; top: 105px; }
  .side-label--notes { left: 34px; top: 998px; }
  .title-monthly {
    position: absolute; left: 60px; top: 28px; font-size: 90px; font-weight: 800;
    color: var(--green); letter-spacing: -1px; line-height: 1;
  }
  .title-budget {
    position: absolute; left: 60px; top: 112px; font-size: 88px; font-weight: 400;
    color: transparent; -webkit-text-stroke: 2px var(--green); line-height: 1; letter-spacing: 1px;
  }
  .contact { position: absolute; left: 435px; top: 58px; color: var(--green); }
  .contact__line { font-size: 15.5px; }
  .contact__line strong { font-weight: 700; }
  .contact__sub { font-size: 10px; margin-top: 1px; }
  .brand {
    position: absolute; right: 30px; top: 70px; display: flex; align-items: center; gap: 6px;
    color: var(--green); font-size: 13px; font-weight: 700; letter-spacing: .5px;
  }
  .brand__dot { width: 12px; height: 12px; border-radius: 50%; background: var(--green); }
  .date-field {
    position: absolute; top: 143px; height: 34px; border: 2.5px solid var(--frame);
    color: #b0b0b0; font-size: 25px; display: flex; align-items: center; justify-content: center;
  }
  .date-field--month { left: 428px; width: 182px; }
  .date-field--year { left: 616px; width: 107px; }
  .col-head {
    position: absolute; top: 209px; color: var(--green); font-size: 18px; font-weight: 600;
    padding-bottom: 2px; border-bottom: 3.5px solid var(--green); text-align: center; white-space: nowrap;
  }
  .col-head--expenses { left: 63px; width: 176px; text-align: left; }
  .col-head--budget { left: 486px; width: 70px; }
  .col-head--actual { left: 672px; width: 62px; }
  .col-hint { position: absolute; font-family: "Didact Gothic", sans-serif; color: var(--grey); text-align: center; }
  .col-hint--category { left: 63px; top: 254px; font-size: 32px; letter-spacing: 1px; }
  .col-hint--budget { left: 449px; width: 150px; top: 258px; font-size: 16px; line-height: 20px; letter-spacing: .5px; }
  .col-hint--actual { left: 629px; width: 150px; top: 258px; font-size: 16px; line-height: 20px; letter-spacing: .5px; }
  .rows { position: absolute; left: 0; top: 0; }
  .notes-box {
    position: absolute; left: 66px; top: 879px; width: 327px; height: 176px; border: 2.5px solid var(--frame);
  }
  .formula__circle {
    position: absolute; width: 106px; height: 106px; border-radius: 50%; background: var(--green-bright);
    color: #fff; display: flex; flex-direction: column; align-items: center; justify-content: center;
    font-family: "Archivo", Arial, sans-serif; font-weight: 500; line-height: 1;
  }
  .formula__circle--net { left: 424px; top: 899px; }
  .formula__circle--gross { left: 572px; top: 897px; }
  .formula__circle--total { left: 711px; top: 897px; }
  .formula__big { font-size: 20px; letter-spacing: 1px; }
  .formula__big + .formula__big { margin-top: 4px; }
  .formula__big--xl { font-size: 34px; }
  .formula__small { font-size: 14px; letter-spacing: 1px; margin-top: 2px; }
  .formula__op { position: absolute; color: var(--green-bright); font-size: 26px; font-weight: 700; }
  .formula__op--eq { left: 539px; top: 932px; }
  .formula__op--minus { left: 689px; top: 930px; }
  .formula__caption {
    position: absolute; width: 120px; text-align: center; font-family: "Didact Gothic", sans-serif;
    font-size: 10px; color: var(--ink-soft); line-height: 12px; letter-spacing: .4px;
  }
  .formula__caption--net { left: 417px; top: 1031px; }
  .formula__caption--gross { left: 565px; top: 1031px; }
  .formula__caption--total { left: 706px; top: 1036px; }
  .decor { position: absolute; }
  .decor--left { left: 0; top: 1066px; width: 266px; height: 134px;
    background: linear-gradient(160deg, #dfe7bf, var(--leaf)); border-top-right-radius: 120px 90px; }
  .decor--right { left: 692px; top: 1066px; width: 156px; height: 134px;
    background: linear-gradient(200deg, #dfe7bf, var(--leaf)); border-top-left-radius: 90px 80px; }
</style>
</head>
<body>
<main class="planner">
  <span class="side-label side-label--basic">basic</span>
  <h1>
    <span class="title-monthly">Monthly</span>
    <span class="title-budget">Budget</span>
  </h1>

  <div class="contact">
    <p class="contact__line">Visit us at <strong>clearpursehq.com</strong></p>
    <p class="contact__sub">For personal financial Advice</p>
  </div>
  <div class="brand"><span class="brand__dot"></span>CLEARPURSE</div>

  <div class="date-field date-field--month">month</div>
  <div class="date-field date-field--year">years</div>

  <h2 class="col-head col-head--expenses">Expenses (Category)</h2>
  <h2 class="col-head col-head--budget">Budget</h2>
  <h2 class="col-head col-head--actual">Actual</h2>

  <p class="col-hint col-hint--category">Custom Category</p>
  <p class="col-hint col-hint--budget">What you plan<br>to spend</p>
  <p class="col-hint col-hint--actual">What actually<br>spent</p>

  <svg class="rows" width="848" height="900" aria-hidden="true">
    <defs>
      <g id="budget-row">
        <line x1="66" y1="0" x2="421" y2="0" stroke="#b4b4b4" stroke-width="1.6"/>
        <circle cx="66" cy="0" r="2.4" fill="#b4b4b4"/>
        <circle cx="421" cy="0" r="2.4" fill="#b4b4b4"/>
        <line x1="451" y1="0" x2="596" y2="0" stroke="#b4b4b4" stroke-width="1.6"/>
        <line x1="451" y1="-2.5" x2="451" y2="2.5" stroke="#b4b4b4" stroke-width="1.4"/>
        <line x1="596" y1="-2.5" x2="596" y2="2.5" stroke="#b4b4b4" stroke-width="1.4"/>
        <line x1="631" y1="0" x2="777" y2="0" stroke="#b4b4b4" stroke-width="1.6"/>
        <line x1="631" y1="-2.5" x2="631" y2="2.5" stroke="#b4b4b4" stroke-width="1.4"/>
        <line x1="777" y1="-2.5" x2="777" y2="2.5" stroke="#b4b4b4" stroke-width="1.4"/>
      </g>
    </defs>
    <use href="#budget-row" y="307"/>
    <use href="#budget-row" y="342"/>
    <use href="#budget-row" y="376"/>
    <use href="#budget-row" y="415"/>
    <use href="#budget-row" y="451"/>
    <use href="#budget-row" y="493"/>
    <use href="#budget-row" y="528"/>
    <use href="#budget-row" y="563"/>
    <use href="#budget-row" y="601"/>
    <use href="#budget-row" y="636"/>
    <use href="#budget-row" y="675"/>
    <use href="#budget-row" y="710"/>
    <use href="#budget-row" y="745"/>
    <use href="#budget-row" y="784"/>
    <use href="#budget-row" y="819"/>
  </svg>

  <span class="side-label side-label--notes">notes</span>
  <div class="notes-box"></div>

  <section class="formula" aria-label="Net income equals gross income minus total expenses">
    <div class="formula__circle formula__circle--net">
      <span class="formula__big formula__big--xl">NET</span>
      <span class="formula__small">INCOME</span>
    </div>
    <span class="formula__op formula__op--eq">=</span>
    <div class="formula__circle formula__circle--gross">
      <span class="formula__big">GROSS</span>
      <span class="formula__big">INCOME</span>
    </div>
    <span class="formula__op formula__op--minus">–</span>
    <div class="formula__circle formula__circle--total">
      <span class="formula__big">TOTAL</span>
      <span class="formula__small">EXPENSES</span>
    </div>
    <p class="formula__caption formula__caption--net">How much money<br>you kept</p>
    <p class="formula__caption formula__caption--gross">How much money<br>you earned</p>
    <p class="formula__caption formula__caption--total">Actual Expenses</p>
  </section>

  <div class="decor decor--left" role="img" aria-label="Outlined green leaf illustration"></div>
  <div class="decor decor--right" role="img" aria-label="Outlined green leaf illustration"></div>
</main>
</body>
</html>
```